Design AND code an HTML landing page

A landing page for campaigns and webinars respondents for project www.brevoa-homes.com. We expect the design to be coded. We will provide the copy and content. It will be a simple landing page for a new development project, to capture details of any potential clients showing interest, including any leads generated via webinars.

Broad instructions are as follows:
- It should not have a header or footer. Minimum escape links as possible.
- Create a lead generator box to get e-mails / relevant info of people interested.
- If possible, add a virtual tour (link to host server provided) at the top of the page.
- Content will be provided
- An option to include a link to a ClipHarbor video

Target Market(s)

Pre/retiree and retirees

Industry/Entity Type

Real estate development, retirement, relocation, travel and tourism

Coding

Coded - Design and coding required

Font styles to use
Other font styles liked:
• Preferably same as existing site

Colors
FFF300
FFF600
FEFA6F
FFFEC7
FFFEE8

Requirements
Must have
• Simple yet appealing look and feel, within the motif of the project, simple list of questions
Should not have
• Emojis, unrelated graphics, excessive graphics that are not linked to project

```html
<!DOCTYPE html>
<html lang="en">
<head>
<meta charset="utf-8">
<title>Brevoa Homes – Campaigns</title>
<link rel="stylesheet" href="https://fonts.googleapis.com/css2?family=Poppins:wght@300;400;500;600&display=swap">
<style>
  :root {
    --yellow: #fbdb05;
    --ink: #000000;
    --text: #222222;
    --muted: #6b6b6b;
    --logo-grey: #4f4f4f;
    --footer-bg: #f7f7f7;
    --sky-top: #3f8fdc;
    --sky-mid: #5fa9e8;
    --building: #e9eef3;
    --red: #ff0000;
    --white: #ffffff;
  }
  * { box-sizing: border-box; margin: 0; padding: 0; }
  html, body { width: 998px; height: 1200px; overflow: hidden; background: var(--white); }
  body { position: relative; font-family: "Poppins", sans-serif; color: var(--text); }

  .hero {
    position: absolute; left: 0; top: 0; width: 998px; height: 547px;
    background: linear-gradient(100deg, var(--sky-top) 0%, var(--sky-mid) 38%, #b9d3ea 48%, var(--building) 62%, #d6dde6 80%, #9fb4c9 100%);
  }
  .brand {
    position: absolute; left: 83px; top: 176px;
    font-weight: 300; font-size: 50px; line-height: 60px;
    color: var(--logo-grey); letter-spacing: -0.5px; white-space: nowrap;
  }

  .btn {
    position: absolute; display: flex; align-items: center; justify-content: center; gap: 10px;
    width: 156px; height: 40px; border-radius: 2px;
    font-weight: 600; font-size: 16px; text-decoration: none;
  }
  .btn svg { width: 22px; height: 10px; }
  .btn-tour { left: 104px; top: 321px; background: var(--yellow); color: var(--ink); }
  .btn-submit { left: 210px; top: 338px; background: var(--ink); color: var(--yellow); border: none; font-family: inherit; }

  .lead-form {
    position: absolute; left: 86px; top: 616px; width: 391px; height: 408px;
    background: var(--yellow); border-radius: 6px;
  }
  .field {
    position: absolute; left: 25px; width: 337px; height: 42px;
    border: 1px solid var(--ink); background: transparent;
    font-family: inherit; font-size: 12.6px; color: var(--ink);
    padding: 0 11px; display: flex; align-items: center;
  }
  .field-name { top: 32px; }
  .field-phone { top: 83px; }
  .field-email { top: 133px; }
  .field-area { top: 185px; justify-content: space-between; }
  .field-area svg { width: 10px; height: 6px; }
  .field-message { top: 235px; height: 92px; width: 338px; align-items: flex-start; padding-top: 12px; }

  .campaigns { position: absolute; left: 522px; top: 610px; width: 392px; }
  .campaigns h1 { font-weight: 600; font-size: 33px; color: var(--ink); line-height: 1.3; }
  .campaigns p { font-size: 12.6px; line-height: 25.5px; color: var(--muted); }
  .campaigns .intro { margin-top: 3px; }
  .campaign-visual {
    width: 390px; height: 195px; margin-top: 12px; border-radius: 5px;
    background: linear-gradient(120deg, #2a2a2a 0%, #6d6d6d 35%, #d9d9d9 55%, #3b3b3b 75%, #1f1f1f 100%);
  }
  .campaigns .caption { margin-top: 12px; }

  .footer {
    position: absolute; left: 0; top: 1089px; width: 998px; height: 111px;
    background: var(--footer-bg); text-align: center;
  }
  .video-link {
    position: absolute; left: 0; right: 0; top: 28px;
    display: flex; align-items: center; justify-content: center; gap: 8px;
    font-size: 14px; font-weight: 500; color: var(--text); text-decoration: none;
  }
  .video-square { width: 16px; height: 16px; background: var(--red); border-radius: 3px; }
  .copyright { position: absolute; left: 0; right: 0; top: 67px; font-size: 14px; color: var(--text); }
</style>
</head>
<body>
  <section class="hero" role="img" aria-label="Photo of a white apartment building with glass balconies against a blue sky with clouds"></section>

  <div class="brand">Brevoa Homes</div>

  <a class="btn btn-tour" href="#">Virtual Tour
    <svg viewBox="0 0 22 10" fill="none" stroke="currentColor" stroke-width="1.6"><path d="M0 5h20M16 1l4 4-4 4"/></svg>
  </a>

  <form class="lead-form">
    <div class="field field-name">Name</div>
    <div class="field field-phone">Phone</div>
    <div class="field field-email">Email</div>
    <div class="field field-area">Area of interest
      <svg viewBox="0 0 10 6"><path d="M0 0h10L5 6z" fill="currentColor"/></svg>
    </div>
    <div class="field field-message">Message</div>
    <button class="btn btn-submit" type="submit">Submit
      <svg viewBox="0 0 22 10" fill="none" stroke="currentColor" stroke-width="1.6"><path d="M0 5h20M16 1l4 4-4 4"/></svg>
    </button>
  </form>

  <section class="campaigns">
    <h1>Campaigns</h1>
    <p class="intro">Lorem ipsum dolor sit amet, consectetur adipiscing elit, sed do eiusmod tempor incint ut labore et dolore magna aliqua. Quis ipsum suspendisse ultrices gravida. Risus commodo viverra maecenas accumsan lacus vel facilisis.</p>
    <div class="campaign-visual" role="img" aria-label="Photo of a smartphone showing media ad cards, resting on a laptop"></div>
    <p class="caption">Lorem ipsum dolor sit amet, consectetur adipiscing elit, sed do eiusmod tempor incint ut labore e</p>
  </section>

  <footer class="footer">
    <a class="video-link" href="#"><span class="video-square"></span>ClipHarbor</a>
    <p class="copyright">© Copyright | brevoa-homes 2022. All Right Reserved</p>
  </footer>
</body>
</html>
```